Mortgage Broking Flyer to attract attention

We are looking for double sided, colour DL sized flyers for a mail drop to inform people what services we offer.
We are a Mortgage Broking Business in Alice Springs NT Australia. Alice Springs is a large country town so we want something that is personal, a little bit playful but still professional, and is going to capture the attention of potential clients when they first look at it so they want to read on.
Please use our logo and colours (red & white) plus a photo of our team – all attached.
Brochure Front: IMPORTANT
Please come up with a tag line based on the following-We want to be seen as different to the bank, more friendly, personable, we listen, want to help and want people to keep coming back even for the little things.
The home page from our website has good dot points but we would like them shorter and to the point www.ochrepeakfinance.com.au
Plus include something which lets customer know that we can assist purchases made through any real estate office, anywhere in Australia
Don’t want the front to contain too many long sentences or paragraphs.
Brochure Back:
Please include:
Services/Specialties
• First home buyers
• Refinancing
• Investments
• Construction loans
• Debt consolidation
• Commercial finance
Please include the following contact details:
Dominic Wexley – Managing Director
Marisol Fenwicke – Loans Consultant
Tamsin Pallister – Loans Consultant
Suite 4/17 Gundry Street, Alice Springs NT 0870
Phone: 08 8927 4158
www.ochrepeakfinance.com.au
We must include the following fine print at the back/bottom of the brochure:
Dominic Wexley (Credit Representative Number: 512873), Marisol Fenwicke (Credit Representative Number: 512874) and Tamsin Pallister (Credit Representative Number: 637215) are credit representatives of QVTRO Pty Ltd (Australian Credit Licence Number: 748016)
Please feel free to email me with any questions.
kerry@ochrepeakfinance.com.au

```html
<!DOCTYPE html>
<html lang="en">
<head>
<meta charset="utf-8">
<title>Ochre Peak Finance – DL Flyer</title>
<link rel="stylesheet" href="https://fonts.googleapis.com/css2?family=Source+Sans+3:ital,wght@0,300;0,400;0,600;0,700;1,400&display=swap">
<style>
:root{
  --red:#e11d25;
  --red-deep:#9e0f16;
  --white:#ffffff;
  --paper:#f3f3f3;
  --grey:#b9b9b9;
  --grey-dark:#6f6f6f;
  --ink:#1a1a1a;
  --stage:#d8d8d6;
}
*{margin:0;padding:0;box-sizing:border-box}
html,body{width:1110px;height:1200px;overflow:hidden}
body{background:var(--stage);position:relative;font-family:"Source Sans 3",Arial,sans-serif;color:var(--white)}
.flyer{position:absolute;width:448px;height:938px;background:var(--paper);box-shadow:0 6px 18px rgba(0,0,0,.35);overflow:hidden}
.flyer--front{left:88px;top:107px}
.flyer--back{left:590px;top:164px}
.flyer-art{position:absolute;inset:0}
.abs{position:absolute;left:0;width:100%;text-align:center}

.brand{position:absolute;left:46px;top:36px;display:flex;align-items:center;gap:16px}
.brand-dot{width:66px;height:66px;border-radius:50%;background:var(--red)}
.brand-name{font-weight:300;font-size:33px;letter-spacing:.5px;color:var(--ink);text-transform:uppercase;line-height:1}

.seal{position:absolute;width:148px;height:148px;border-radius:50%;background:var(--white);border:6px solid #d6d6d6;box-shadow:0 3px 8px rgba(0,0,0,.35);display:flex;align-items:center;justify-content:center;text-align:center}
.seal-name{font-weight:600;font-size:20px;line-height:1.1;color:var(--red);text-transform:uppercase}
.flyer--front .seal{left:270px;top:422px}
.flyer--back .seal{left:294px;top:232px}

.headline{top:604px;font-weight:400;font-size:30px;line-height:34px;text-transform:uppercase}
.no-cost{top:706px;font-size:17px;font-weight:400;text-transform:uppercase;letter-spacing:-.2px}
.rule{position:absolute;height:2px;background:linear-gradient(90deg,rgba(255,255,255,0),rgba(235,235,235,.95),rgba(255,255,255,0))}
.flyer--front .rule{left:32px;width:384px;top:740px}
.any-office{top:752px;font-style:italic;font-size:17px;line-height:21px}

.contact{top:842px;color:var(--ink)}
.contact-title{font-weight:600;font-size:15px;line-height:20px}
.contact-phone{font-weight:600;font-size:20px;line-height:26px;display:flex;justify-content:center;align-items:center;gap:8px}
.contact-phone svg{width:20px;height:20px}
.contact-web{font-weight:700;font-size:15px;color:var(--red);line-height:20px}
.contact-address{font-size:14px;line-height:22px;letter-spacing:.3px}

.intro{top:396px;font-style:italic;font-size:17px;line-height:20px;color:#fbe3e3}
.tab{position:absolute;left:0;top:462px;width:234px;height:32px;background:linear-gradient(#f4f4f4,#cfcfcf);border-radius:0 16px 16px 0;color:var(--red);font-weight:700;font-size:19px;line-height:32px;padding-left:22px;text-transform:uppercase}
.services{position:absolute;left:22px;top:504px;list-style:none}
.services li{display:flex;align-items:center;gap:9px;font-size:20px;line-height:26px}
.services svg{width:15px;height:15px;flex:none}
.team{top:680px;font-size:19px;line-height:24px}
.team em{font-size:17px}
.flyer--back .rule{left:44px;width:380px;top:766px}
.back-web{top:776px;font-size:21px;letter-spacing:.3px}
.fine-print{position:absolute;left:30px;width:388px;top:878px;text-align:center;font-size:9.5px;line-height:12.5px;color:var(--ink)}
.fine-print b{font-weight:600}
</style>
</head>
<body>

<section class="flyer flyer--front" aria-label="Flyer front">
  <svg class="flyer-art" width="448" height="938" viewBox="0 0 448 938">
    <defs>
      <linearGradient id="frontRed" x1="0" y1="0" x2="0" y2="1">
        <stop offset="0" stop-color="#e4222a"/><stop offset=".55" stop-color="#c4161e"/><stop offset="1" stop-color="#8f0c12"/>
      </linearGradient>
      <linearGradient id="frontLand" x1="0" y1="0" x2="0" y2="1">
        <stop offset="0" stop-color="#8a93a8"/><stop offset=".35" stop-color="#c7845a"/><stop offset=".65" stop-color="#7d7a5c"/><stop offset="1" stop-color="#b8893a"/>
      </linearGradient>
      <linearGradient id="swoosh" x1="0" y1="0" x2="1" y2="0">
        <stop offset="0" stop-color="#7a7a7a"/><stop offset=".6" stop-color="#d0d0d0"/><stop offset="1" stop-color="#f2f2f2"/>
      </linearGradient>
    </defs>
    <rect width="448" height="938" fill="#f5f5f5"/>
    <path role="img" aria-label="Photo of a ridge in the desert ranges at sunset" d="M0,168 Q230,125 448,96 L448,450 Q250,520 0,540 Z" fill="url(#frontLand)"/>
    <path d="M0,150 Q230,108 448,84 L448,100 Q230,128 0,180 Z" fill="url(#swoosh)"/>
    <path d="M0,528 Q250,510 448,440 L448,938 L0,938 Z" fill="url(#frontRed)"/>
    <path d="M0,518 Q250,500 448,430 L448,446 Q250,518 0,538 Z" fill="url(#swoosh)"/>
    <path d="M0,850 Q224,792 448,850" fill="none" stroke="#c9c9c9" stroke-width="5"/>
    <path d="M0,852 Q224,796 448,852 L448,938 L0,938 Z" fill="#f4f4f4"/>
  </svg>

  <div class="brand"><span class="brand-dot"></span><span class="brand-name">Ochre Peak Finance</span></div>
  <div class="seal"><span class="seal-name">Ochre<br>Peak</span></div>

  <h1 class="abs headline">Home loans styled to<br>your needs</h1>
  <p class="abs no-cost">No cost to you.</p>
  <div class="rule"></div>
  <p class="abs any-office">We can assist purchases made through any<br>real estate office, anywhere in Australia</p>

  <div class="abs contact">
    <p class="contact-title">Contact Us Today</p>
    <p class="contact-phone">
      <svg viewBox="0 0 20 20" aria-hidden="true"><circle cx="10" cy="10" r="9" fill="none" stroke="#1a1a1a" stroke-width="1.6"/><path d="M6.3 5.2l2 .1.8 2.4-1.2 1a6 6 0 0 0 3.4 3.4l1-1.2 2.4.8.1 2c-3.8.7-9.2-4.7-8.5-8.5z" fill="#1a1a1a"/></svg>
      (08) 8927 4158
    </p>
    <p class="contact-web">www.ochrepeakfinance.com.au</p>
    <p class="contact-address">Suite 4/17 Gundry Street, Alice Springs</p>
  </div>
</section>

<section class="flyer flyer--back" aria-label="Flyer back">
  <svg class="flyer-art" width="448" height="938" viewBox="0 0 448 938">
    <defs>
      <linearGradient id="backRed" x1="0" y1="0" x2="0" y2="1">
        <stop offset="0" stop-color="#e4222a"/><stop offset=".6" stop-color="#c4161e"/><stop offset="1" stop-color="#8f0c12"/>
      </linearGradient>
      <linearGradient id="team" x1="0" y1="0" x2="1" y2="1">
        <stop offset="0" stop-color="#6e7358"/><stop offset=".5" stop-color="#a9a89a"/><stop offset="1" stop-color="#8e8f7e"/>
      </linearGradient>
      <linearGradient id="swoosh2" x1="0" y1="0" x2="1" y2="0">
        <stop offset="0" stop-color="#8a8a8a"/><stop offset=".55" stop-color="#d4d4d4"/><stop offset="1" stop-color="#f4f4f4"/>
      </linearGradient>
    </defs>
    <rect width="448" height="938" fill="url(#backRed)"/>
    <path role="img" aria-label="Team photo of the three consultants standing under a tree" d="M0,0 L448,0 L448,262 Q250,345 0,360 Z" fill="url(#team)"/>
    <path d="M0,352 Q250,338 448,255 L448,275 Q250,360 0,374 Z" fill="url(#swoosh2)"/>
    <path d="M0,838 Q224,782 448,838" fill="none" stroke="#c9c9c9" stroke-width="5"/>
    <path d="M0,840 Q224,786 448,840 L448,938 L0,938 Z" fill="#f4f4f4"/>
  </svg>

  <div class="seal"><span class="seal-name">Ochre<br>Peak</span></div>

  <p class="abs intro">We understand that everyone’s financial situations<br>are unique and we will tailor a home loan to suit your needs.</p>

  <h2 class="tab">Services/Specialties</h2>
  <ul class="services">
    <li><svg viewBox="0 0 16 16" aria-hidden="true"><circle cx="8" cy="8" r="7.5" fill="#e6e6e6"/><path d="M6.5 4.5 10 8l-3.5 3.5" fill="none" stroke="#b3141b" stroke-width="2"/></svg>First home buyers</li>
    <li><svg viewBox="0 0 16 16" aria-hidden="true"><circle cx="8" cy="8" r="7.5" fill="#e6e6e6"/><path d="M6.5 4.5 10 8l-3.5 3.5" fill="none" stroke="#b3141b" stroke-width="2"/></svg>Refinancing</li>
    <li><svg viewBox="0 0 16 16" aria-hidden="true"><circle cx="8" cy="8" r="7.5" fill="#e6e6e6"/><path d="M6.5 4.5 10 8l-3.5 3.5" fill="none" stroke="#b3141b" stroke-width="2"/></svg>Investments</li>
    <li><svg viewBox="0 0 16 16" aria-hidden="true"><circle cx="8" cy="8" r="7.5" fill="#e6e6e6"/><path d="M6.5 4.5 10 8l-3.5 3.5" fill="none" stroke="#b3141b" stroke-width="2"/></svg>Construction loans</li>
    <li><svg viewBox="0 0 16 16" aria-hidden="true"><circle cx="8" cy="8" r="7.5" fill="#e6e6e6"/><path d="M6.5 4.5 10 8l-3.5 3.5" fill="none" stroke="#b3141b" stroke-width="2"/></svg>Debt consolidation</li>
    <li><svg viewBox="0 0 16 16" aria-hidden="true"><circle cx="8" cy="8" r="7.5" fill="#e6e6e6"/><path d="M6.5 4.5 10 8l-3.5 3.5" fill="none" stroke="#b3141b" stroke-width="2"/></svg>Commercial finance</li>
  </ul>

  <div class="abs team">
    <p>Dominic Wexley – <em>Managing Director</em></p>
    <p>Marisol Fenwicke – <em>Loans Consultant</em></p>
    <p>Tamsin Pallister – <em>Loans Consultant</em></p>
  </div>
  <div class="rule"></div>
  <p class="abs back-web">www.ochrepeakfinance.com.au</p>

  <p class="fine-print"><b>Dominic Wexley</b> (Credit Representative Number: 512873), <b>Marisol Fenwicke</b> (Credit Representative Number: 512874) and <b>Tamsin Pallister</b> (Credit Representative Number: 637215) are credit representatives of QVTRO Pty Ltd (Australian Credit Licence Number: 748016)</p>
</section>

</body>
</html>
```